Timber Ridge Land Services Business Cards

Need to create a business card with the company logo "Timber Ridge Land Services". The business will provide forestry mulching for land clearing and vegetation control, brush and small tree removal, wildlife habitat improvement and trail and property access creation.

```html
<!DOCTYPE html>
<html lang="en">
<head>
<meta charset="utf-8">
<title>Timber Ridge Land Services – Business Card</title>
<link href="https://fonts.googleapis.com/css2?family=Lato:wght@400;700;900&display=swap" rel="stylesheet">
<style>
  :root {
    --stage: #d9d9d9;
    --card: #ffffff;
    --green-dark: #0f5b37;
    --green-dot: #5fb55a;
    --text-grey: #585858;
    --yellow: #f5e63a;
    --photo-field: #7f9a5a;
    --photo-sky: #c9cfc0;
    --photo-brush: #4f7d2e;
    --photo-deep: #2f5a22;
  }
  * { box-sizing: border-box; margin: 0; padding: 0; }
  html, body {
    width: 1200px; height: 788px; overflow: hidden;
    background: var(--stage);
    font-family: "Lato", sans-serif;
  }
  .card {
    position: absolute; left: 50px; top: 64px;
    width: 1100px; height: 660px;
    background: var(--card);
    overflow: hidden;
  }
  .photo-panel { position: absolute; inset: 0; width: 1100px; height: 660px; }
  .brand {
    position: absolute; left: 52px; top: 128px;
    color: var(--green-dark); font-weight: 900;
    text-transform: uppercase; line-height: 1;
  }
  .brand-name { font-size: 36px; letter-spacing: 0.5px; }
  .brand-sub { font-size: 21px; letter-spacing: 1px; margin-top: 8px; }
  .services {
    position: absolute; left: 56px; top: 240px; width: 560px;
    list-style: none;
  }
  .services li {
    position: relative; padding-left: 24px; margin-bottom: 18px;
    font-size: 20px; font-weight: 700; color: var(--text-grey);
    text-transform: uppercase; letter-spacing: 0.6px; line-height: 25px;
  }
  .services li::before {
    content: ""; position: absolute; left: 0; top: 7px;
    width: 14px; height: 14px; border-radius: 50%;
    background: var(--green-dot);
  }
  .cta-box {
    position: absolute; left: 47px; top: 432px;
    width: 476px; height: 140px;
    border: 3px solid var(--yellow); border-radius: 10px;
    text-align: center; padding-top: 20px;
    color: var(--green-dark); font-size: 28px; letter-spacing: 0.8px;
    text-transform: uppercase; line-height: 36px;
  }
  .cta-lead { font-weight: 700; }
  .cta-free strong { font-weight: 900; }
  .phone-pill {
    position: absolute; left: 115px; top: 536px;
    width: 344px; height: 66px; border-radius: 33px;
    background: var(--yellow);
    display: flex; align-items: center;
  }
  .phone-icon {
    width: 54px; height: 54px; margin-left: 4px; border-radius: 50%;
    background: var(--green-dark);
    display: flex; align-items: center; justify-content: center;
  }
  .phone-number {
    margin-left: 26px; font-size: 29px; font-weight: 900;
    color: #1e2a1e; letter-spacing: 1px;
  }
</style>
</head>
<body>
  <section class="card">
    <svg class="photo-panel" viewBox="0 0 1100 660" xmlns="http://www.w3.org/2000/svg">
      <defs>
        <linearGradient id="savannaTone" x1="0" y1="0" x2="0" y2="1">
          <stop offset="0" stop-color="var(--photo-sky)"/>
          <stop offset="0.45" stop-color="#a7ad8a"/>
          <stop offset="1" stop-color="var(--photo-field)"/>
        </linearGradient>
        <linearGradient id="brushTone" x1="0" y1="0" x2="1" y2="1">
          <stop offset="0" stop-color="var(--photo-brush)"/>
          <stop offset="1" stop-color="var(--photo-deep)"/>
        </linearGradient>
      </defs>
      <polygon class="photo-wildlife" role="img" aria-label="Photo of a savanna with a tree and wildlife"
               points="446,0 949,0 847,407 679,242" fill="url(#savannaTone)"/>
      <polygon class="photo-crew" role="img" aria-label="Photo of a worker clearing brush with a trimmer"
               points="949,0 1100,0 1100,660 558,660 679,242 847,407" fill="url(#brushTone)"/>
      <polyline points="446,0 679,242 558,660" fill="none" stroke="var(--yellow)" stroke-width="8"/>
      <polyline points="949,0 847,407 679,242" fill="none" stroke="var(--yellow)" stroke-width="7"/>
    </svg>

    <div class="brand">
      <div class="brand-name">Timber Ridge</div>
      <div class="brand-sub">Land Services</div>
    </div>

    <ul class="services">
      <li>Forestry mulching for land clearing<br>and vegetation control</li>
      <li>Brush and small tree removal</li>
      <li>Wildlife habitat improvement and trail<br>and property access creation</li>
    </ul>

    <div class="cta-box">
      <div class="cta-lead">Call us for a</div>
      <div class="cta-free"><strong>Free</strong> estimate today!</div>
    </div>

    <div class="phone-pill">
      <span class="phone-icon">
        <svg width="28" height="28" viewBox="0 0 24 24" aria-hidden="true">
          <path fill="#ffffff" d="M6.6 10.8c1.4 2.8 3.8 5.1 6.6 6.6l2.2-2.2c.3-.3.7-.4 1-.2 1.1.4 2.3.6 3.6.6.6 0 1 .4 1 1V20c0 .6-.4 1-1 1C10.6 21 3 13.4 3 4c0-.6.4-1 1-1h3.5c.6 0 1 .4 1 1 0 1.3.2 2.5.6 3.6.1.3 0 .7-.2 1l-2.3 2.2z"/>
          <path fill="none" stroke="#ffffff" stroke-width="1.6" stroke-linecap="round" d="M14.5 3.5a6.5 6.5 0 0 1 6 6M14.5 6.8a3.3 3.3 0 0 1 2.8 2.8"/>
        </svg>
      </span>
      <span class="phone-number">123-456-7890</span>
    </div>
  </section>
</body>
</html>
```